Business Cards Design for the electrical wholesaler: clean bold dynamic :)

We need a business card design that would follow our latest brand guidelines. As an electrical wholesaler we want to bring a fresh look and feel into the industry. The design should be clean bold and dynamic. It should come alive with the renewed energy of our green colour. Our grey colour should keep things balanced and complement the notion of maturity and responsibility. We employ Lato as a corporate font however are not bound by this font and we’re open to interpretation here.

Target Market(s)

Electrical contractors

Industry/Entity Type

Business

Contact Information for Business Card

Logo
Name & Surname: Olena Dovbush
Job Title: Director of Marketing
Email: helen.dovbush@mailvane.example
Cell phone: XXX.XXX.XXXX
Address: 20917 - 87 Ave. Edmonton, AB, Canada. T6K 2R8
Business Phone: 780.555.0187
Website: www.qorvil.example

Font styles to use
Other font styles liked:
• Lato

Requirements
Must have
• Logo & website
Nice to have
• Brand elements - some of them you may find in the attached Brand Guidelines (e.g. three lines on the background signifying "W")

```html
<!DOCTYPE html>
<html lang="en">
<head>
<meta charset="utf-8">
<title>Qorvil Business Card</title>
<link rel="stylesheet" href="https://fonts.googleapis.com/css2?family=Lato:wght@300;400;700;900&display=swap">
<style>
  :root {
    --brand-green: #6cc12a;
    --brand-grey: #3a3a3c;
    --text-grey: #4a4a4c;
    --soft-grey: #9a9a9c;
    --rule-grey: #d6d6d6;
    --card-white: #ffffff;
    --page-bg: #efefef;
  }
  * { box-sizing: border-box; margin: 0; padding: 0; }
  html, body {
    width: 1115px;
    height: 1200px;
    overflow: hidden;
    background: var(--page-bg);
    font-family: "Lato", Arial, sans-serif;
  }
  .sheet {
    position: relative;
    width: 1115px;
    height: 1200px;
  }
  .card {
    position: absolute;
    left: 107px;
    width: 900px;
    height: 514px;
    overflow: hidden;
    box-shadow: 0 6px 22px rgba(0,0,0,0.12);
  }
  .card--front { top: 60px; background: var(--card-white); }
  .card--back  { top: 626px; background: var(--brand-green); }

  /* Brand lockup */
  .brand {
    position: absolute;
    display: flex;
    align-items: center;
    gap: 14px;
  }
  .brand__square {
    width: 34px;
    height: 34px;
    background: var(--brand-green);
  }
  .brand__name {
    font-weight: 900;
    font-size: 58px;
    line-height: 1;
    letter-spacing: -1px;
    color: var(--brand-grey);
  }
  .brand__tagline {
    position: absolute;
    font-weight: 700;
    font-size: 11px;
    letter-spacing: 3px;
    color: var(--brand-green);
    text-transform: uppercase;
  }
  .card--front .brand { left: 262px; top: 84px; }
  .card--front .brand__tagline { left: 420px; top: 150px; }

  .card--back .brand { left: 300px; top: 200px; }
  .card--back .brand__square { background: var(--card-white); }
  .card--back .brand__name { color: var(--card-white); font-size: 72px; }
  .card--back .brand__tagline { left: 460px; top: 284px; color: var(--card-white); }

  /* Person */
  .person {
    position: absolute;
    left: 110px;
    top: 222px;
  }
  .person__name {
    font-weight: 400;
    font-size: 30px;
    letter-spacing: 1px;
    text-transform: uppercase;
    color: var(--brand-grey);
  }
  .person__role {
    margin-top: 6px;
    font-weight: 400;
    font-size: 14px;
    letter-spacing: 3px;
    text-transform: uppercase;
    color: var(--soft-grey);
  }

  /* Stripes */
  .stripe-left {
    position: absolute;
    left: 0;
    top: 318px;
    width: 400px;
    height: 7px;
    background: var(--brand-green);
  }
  .divider {
    position: absolute;
    left: 438px;
    top: 262px;
    width: 2px;
    height: 140px;
    background: var(--rule-grey);
  }
  .stripe-bottom {
    position: absolute;
    left: 400px;
    bottom: 0;
    width: 360px;
    height: 14px;
    background: var(--brand-green);
  }
  .stripe-bottom--grey {
    left: 760px;
    width: 140px;
    background: var(--brand-grey);
  }

  /* Contacts */
  .contacts {
    position: absolute;
    left: 468px;
    top: 264px;
    list-style: none;
  }
  .contacts__item {
    display: flex;
    align-items: center;
    gap: 12px;
    height: 26px;
    font-size: 16px;
    white-space: nowrap;
    color: var(--text-grey);
  }
  .contacts__icon {
    width: 16px;
    height: 16px;
    flex: none;
  }
</style>
</head>
<body>
<main class="sheet">

  <section class="card card--front" aria-label="Business card front">
    <div class="brand">
      <span class="brand__square"></span>
      <span class="brand__name">qorvil</span>
    </div>
    <span class="brand__tagline">Electrical Wholesalers</span>

    <div class="person">
      <p class="person__name">Olena Dovbush</p>
      <p class="person__role">Director of Marketing</p>
    </div>

    <span class="stripe-left"></span>
    <span class="divider"></span>

    <ul class="contacts">
      <li class="contacts__item">
        <svg class="contacts__icon" viewBox="0 0 16 16"><rect width="16" height="16" rx="3" fill="#6cc12a"/><path d="M5 3.5h2l1 2.5-1.3 1a6 6 0 0 0 2.3 2.3l1-1.3 2.5 1v2a1 1 0 0 1-1 1A8.5 8.5 0 0 1 4 4.5a1 1 0 0 1 1-1z" fill="#fff"/></svg>
        780.555.0187
      </li>
      <li class="contacts__item">
        <svg class="contacts__icon" viewBox="0 0 16 16"><rect width="16" height="16" rx="3" fill="#6cc12a"/><rect x="5" y="2.5" width="6" height="11" rx="1.2" fill="#fff"/><circle cx="8" cy="11.6" r="0.8" fill="#6cc12a"/></svg>
        780.555.0142
      </li>
      <li class="contacts__item">
        <svg class="contacts__icon" viewBox="0 0 16 16"><rect width="16" height="16" rx="3" fill="#6cc12a"/><rect x="3" y="4.5" width="10" height="7" fill="#fff"/><path d="M3 4.5l5 4 5-4" fill="none" stroke="#6cc12a" stroke-width="1.2"/></svg>
        helen.dovbush@mailvane.example
      </li>
      <li class="contacts__item">
        <svg class="contacts__icon" viewBox="0 0 16 16"><rect width="16" height="16" rx="3" fill="#6cc12a"/><path d="M8 2.8a3.6 3.6 0 0 0-3.6 3.6C4.4 9.2 8 13.2 8 13.2s3.6-4 3.6-6.8A3.6 3.6 0 0 0 8 2.8z" fill="#fff"/><circle cx="8" cy="6.4" r="1.3" fill="#6cc12a"/></svg>
        20917 - 87 Ave. Edmonton, AB, Canada. T6K 2R8
      </li>
      <li class="contacts__item">
        <svg class="contacts__icon" viewBox="0 0 16 16"><rect width="16" height="16" rx="3" fill="#6cc12a"/><circle cx="8" cy="8" r="4.8" fill="none" stroke="#fff" stroke-width="1.2"/><path d="M3.2 8h9.6M8 3.2c-2 2.6-2 7 0 9.6M8 3.2c2 2.6 2 7 0 9.6" fill="none" stroke="#fff" stroke-width="1"/></svg>
        www.qorvil.example
      </li>
    </ul>

    <span class="stripe-bottom"></span>
    <span class="stripe-bottom stripe-bottom--grey"></span>
  </section>

  <section class="card card--back" aria-label="Business card back">
    <div class="brand">
      <span class="brand__square"></span>
      <span class="brand__name">qorvil</span>
    </div>
    <span class="brand__tagline">Electrical Wholesalers</span>
  </section>

</main>
</body>
</html>
```